A-Stand Directional Sign Design

Objective:
We need a professional graphic design for an A-Stand sign that will guide customers arriving in our parking lot to our office. The design should be visually clear, welcoming, and aligned with our brand identity.
REQUIREMENTS:
Two versions of the design:
- One with an arrow pointing left
- One with an arrow pointing right
(This allows us to place the A-Stand anywhere and flip the graphic as needed.)
DIMENSIONS:
- Viewable Area: 30" x 40"
BRAND ALIGNMENT:
- Colors, fonts, and overall style should match our website: www.skornabel.com
- Clean, modern, and professional look consistent with our aviation/tourism brand
CONTENT:
- Clear directional arrow (left or right depending on version)
- Text: “Office Entrance” or similar concise wording (designers may propose alternatives if they improve clarity)
READABILITY:
- Bold, high-contrast design for visibility from a distance
- Simple layout that avoids clutter
DELIVERABLES:
- Final artwork in print-ready format (PDF preferred)
- Two versions: Arrow Left and Arrow Right
DESIGN GOAL:
Ensure customers can easily find our office upon arrival, while reinforcing skorNABEL’s professional and welcoming brand image.
Target Market(s)
Tourism

```html
<!DOCTYPE html>
<html lang="en">
<head>
<meta charset="utf-8">
<title>skorNABEL – Office Entrance A-Stand</title>
<link rel="stylesheet" href="https://fonts.googleapis.com/css2?family=Montserrat:wght@500&family=Lato:wght@900&family=Oswald:wght@500&display=swap">
<style>
  :root {
    --brand-blue: #1f77bb;
    --brand-sky: #86acd9;
    --paper: #ffffff;
    --backdrop: #e2e8f0;
  }
  html, body {
    margin: 0;
    padding: 0;
    width: 1200px;
    height: 2309px;
    overflow: hidden;
    background: var(--backdrop);
  }
  .sign {
    position: absolute;
    left: 40px;
    top: 406px;
    width: 1120px;
    height: 1496px;
  }
  .sign svg { display: block; width: 100%; height: 100%; }
  .brand-name {
    font-family: "Montserrat", sans-serif;
    font-weight: 500;
    fill: var(--brand-blue);
  }
  .direction-label {
    font-family: "Oswald", sans-serif;
    font-weight: 500;
    fill: var(--paper);
    letter-spacing: 1px;
  }
  .web-address {
    font-family: "Lato", sans-serif;
    font-weight: 900;
    fill: var(--paper);
  }
</style>
</head>
<body>
  <main class="sign">
    <svg viewBox="0 0 900 1202" xmlns="http://www.w3.org/2000/svg">
      <defs>
        <linearGradient id="cabin-tones" x1="0" y1="0" x2="1" y2="1">
          <stop offset="0" stop-color="#c9b9a8"/>
          <stop offset="1" stop-color="#3b4a4f"/>
        </linearGradient>
        <linearGradient id="flight-tones" x1="0" y1="0" x2="0" y2="1">
          <stop offset="0" stop-color="#d9e6ec"/>
          <stop offset="0.5" stop-color="#6fa3b0"/>
          <stop offset="1" stop-color="#2f3d44"/>
        </linearGradient>
      </defs>

      <rect class="sign-panel" width="900" height="1202" fill="var(--paper)"/>

      <g class="brand-lockup">
        <circle cx="450" cy="140" r="62" fill="var(--brand-blue)"/>
        <text class="brand-name" x="450" y="325" font-size="80" text-anchor="middle" letter-spacing="2">skorNABEL</text>
        <line x1="162" y1="357" x2="540" y2="357" stroke="var(--brand-blue)" stroke-width="4"/>
        <text class="brand-name" x="738" y="372" font-size="44" text-anchor="end" letter-spacing="10">.com</text>
      </g>

      <g class="photo-frame photo-frame--left" transform="translate(250 636) rotate(-44)">
        <ellipse cx="12" cy="-12" rx="236" ry="152" fill="var(--brand-sky)"/>
        <ellipse cx="-12" cy="12" rx="236" ry="152" fill="var(--brand-blue)"/>
        <ellipse cx="0" cy="0" rx="232" ry="146" fill="var(--paper)"/>
        <ellipse cx="0" cy="0" rx="222" ry="138" fill="url(#cabin-tones)" role="img" aria-label="Photo: smiling passengers with headsets inside a helicopter cabin"/>
      </g>

      <g class="photo-frame photo-frame--right" transform="translate(648 636) rotate(-44)">
        <ellipse cx="12" cy="-12" rx="236" ry="152" fill="var(--brand-sky)"/>
        <ellipse cx="-12" cy="12" rx="236" ry="152" fill="var(--brand-blue)"/>
        <ellipse cx="0" cy="0" rx="232" ry="146" fill="var(--paper)"/>
        <ellipse cx="0" cy="0" rx="222" ry="138" fill="url(#flight-tones)" role="img" aria-label="Photo: pilot with headset flying over a coastal city"/>
      </g>

      <g class="direction-arrow">
        <path d="M142 903 H672 V868 L757 953 L672 1038 V1003 H142 Z" fill="var(--brand-blue)"/>
        <text class="direction-label" x="170" y="980" font-size="64">OFFICE ENTRANCE</text>
      </g>

      <g class="footer-band">
        <path d="M0 1120 Q450 1030 900 1120 V1202 H0 Z" fill="var(--brand-blue)"/>
        <text class="web-address" x="450" y="1162" font-size="56" text-anchor="middle">www.skornabel.com</text>
      </g>
    </svg>
  </main>
</body>
</html>
```